Square Business Cards for Our Restaurant / Event Venue

We need square business cards designed for the management team of our event venue and restaurant. On one side of the card should be the the Harbor Lantern 7 logo and URL www.harborlantern7.example. On the other side should be the Ember Logo and URL www.emberhall7.example. All employee details should be on the side with Ember logo. There will be a total of 5 cards to be created with the design.

Clara Bennquist
clara@harborlantern7.example

main 555.418.3072
direct 555.730.2946

4831 West Orchard Lane SE
Washington, DC 90417

Industry/Entity Type

Business

```html
<!DOCTYPE html>
<html lang="en">
<head>
<meta charset="utf-8">
<title>Harbor Lantern 7 / Ember — Business Cards</title>
<link rel="stylesheet" href="https://fonts.googleapis.com/css2?family=Lato:wght@400;700;900&display=swap">
<style>
  :root {
    --stage: #e6e6e6;
    --ink: #111111;
    --card-dark: #000000;
    --card-light: #ffffff;
    --accent: #b52025;
    --text-light: #ffffff;
  }
  * { box-sizing: border-box; margin: 0; padding: 0; }
  html, body { width: 1200px; height: 880px; overflow: hidden; }
  body {
    background: var(--stage);
    font-family: "Lato", Arial, sans-serif;
    color: var(--ink);
    position: relative;
  }
  .card {
    position: absolute;
    width: 640px;
    height: 366px;
    box-shadow: 0 6px 18px rgba(0,0,0,0.18);
  }
  /* Front: venue side */
  .card--venue {
    left: 80px; top: 60px;
    background: var(--card-dark);
  }
  .venue-mark {
    position: absolute;
    left: 0; right: 0; top: 118px;
    display: flex; align-items: center; justify-content: center; gap: 18px;
  }
  .venue-mark__dot {
    width: 84px; height: 84px; border-radius: 50%;
    background: var(--accent);
  }
  .venue-mark__name {
    font-weight: 700; font-size: 34px; color: var(--text-light);
    letter-spacing: 0.5px;
  }
  .venue-url {
    position: absolute; left: 0; right: 0; bottom: 58px;
    text-align: center; color: var(--accent); font-size: 15px;
  }
  /* Back: employee side */
  .card--staff {
    left: 480px; top: 454px;
    background: var(--card-light);
  }
  .brand {
    position: absolute; left: 48px; top: 54px;
    font-weight: 900; font-size: 64px; color: var(--ink); line-height: 1;
  }
  .staff-name {
    position: absolute; left: 96px; top: 150px;
    font-weight: 900; font-size: 19px;
  }
  .contact-list {
    position: absolute; left: 96px; top: 192px;
    list-style: none; font-size: 16px; line-height: 1;
  }
  .contact-list li {
    display: flex; align-items: center; gap: 10px; height: 26px;
  }
  .contact-list .icon { width: 18px; height: 18px; flex: none; }
  .contact-list .highlight { color: var(--accent); }
  .address {
    position: absolute; right: 40px; bottom: 120px;
    text-align: right; font-size: 15px; line-height: 1.35;
  }
</style>
</head>
<body>

<section class="card card--venue" aria-label="Venue side of the card">
  <div class="venue-mark">
    <span class="venue-mark__dot"></span>
    <span class="venue-mark__name">Harbor Lantern 7</span>
  </div>
  <p class="venue-url">www.harborlantern7.example</p>
</section>

<section class="card card--staff" aria-label="Employee side of the card">
  <p class="brand">Ember</p>
  <p class="staff-name">Clara Bennquist</p>
  <ul class="contact-list">
    <li>
      <svg class="icon" viewBox="0 0 18 18" aria-hidden="true"><circle cx="9" cy="9" r="8.5" fill="#b52025"/><path d="M5.5 6.5c1 3 3 5 6 6l1.2-1.5-1.8-1-1 .8c-1-.5-2-1.5-2.5-2.5l.8-1-1-1.8z" fill="#fff"/></svg>
      <span>555.418.3072</span>
    </li>
    <li>
      <svg class="icon" viewBox="0 0 18 18" aria-hidden="true"><circle cx="9" cy="9" r="8.5" fill="none" stroke="#b52025"/><rect x="6" y="4" width="6" height="10" rx="1" fill="none" stroke="#b52025"/><circle cx="9" cy="12.3" r="0.7" fill="#b52025"/></svg>
      <span>555.730.2946</span>
    </li>
    <li>
      <svg class="icon" viewBox="0 0 18 18" aria-hidden="true"><circle cx="9" cy="9" r="8.5" fill="#b52025"/><rect x="4.5" y="6" width="9" height="6.5" fill="#fff"/><path d="M4.5 6l4.5 3.5L13.5 6" fill="none" stroke="#b52025" stroke-width="1"/></svg>
      <span>clara@harborlantern7.example</span>
    </li>
    <li>
      <svg class="icon" viewBox="0 0 18 18" aria-hidden="true"><circle cx="9" cy="9" r="8.5" fill="#b52025"/><circle cx="9" cy="9" r="4.5" fill="none" stroke="#fff"/><ellipse cx="9" cy="9" rx="2" ry="4.5" fill="none" stroke="#fff"/><line x1="4.5" y1="9" x2="13.5" y2="9" stroke="#fff"/></svg>
      <span>www.<span class="highlight">emberhall7</span>.example</span>
    </li>
  </ul>
  <address class="address" style="font-style:normal">
    4831 West Orchard Lane SE<br>
    Washington, DC 90417
  </address>
</section>

</body>
</html>
```